Hair salon and Nail salon in Hawaii need a newspaper Ad design.

We need a newspaper Ad design for new open hair & nail salon in Waikiki Hawaii.Our Recommendation service for hair is "Head Spa" $30+tax and for nail is "Manicure Treatment Course" (Filing+Cuticle Care+Massage+Coloring) $20+tax.
We would like to see Hawaiian taste color and also having sense of luxury design. The ad size is W 5.0” x H 6.375”.
I would customers to know the shop place(Lanakila Crest Hotel 1F) , phone(808-555-0173), instagram(salonbrightwave) , our web site https://salonbrightwave.example and recommend services. For Web or Instagram , QR code is acceptable.

Target Market(s)

women & men

Industry/Entity Type

Beauty Salon

Font styles to use
Serif

Colors

Designer to choose colors to be used in the design.

Requirements
Must have
• Tagline for local customers. Shop Name is "SALON BRIGHTWAVE".the shop place(Lanakila Crest Hotel 1F) , phone(808-555-0173), instagram(salonbrightwave) and recommend services.
Nice to have
• Our services are competitive, but we don't want to be seen as just cheap and low quality.

```html
<!DOCTYPE html>
<html lang="en">
<head>
<meta charset="utf-8">
<title>Salon Brightwave – Newspaper Ad</title>
<link rel="stylesheet" href="https://fonts.googleapis.com/css2?family=Marcellus&family=Bitter:ital,wght@1,800&family=Ubuntu:ital,wght@0,400;0,500;1,400&family=Montserrat:wght@500;600&family=Noto+Serif:wght@400;700&display=swap">
<style>
  :root {
    --backdrop: #b6b5a7;
    --ink-dark: #120d0b;
    --gold: #b08a5b;
    --gold-light: #c9a474;
    --bronze-start: #3f2a18;
    --bronze-end: #9b6a33;
    --teal-start: #1f5e5e;
    --teal-end: #6aa6aa;
    --band-brown: #8a5e2e;
    --band-shadow: #4a3220;
    --white: #ffffff;
  }
  * { margin: 0; padding: 0; box-sizing: border-box; }
  html, body { width: 1200px; height: 941px; overflow: hidden; background: var(--backdrop); }

  .ad {
    position: absolute; left: 217px; top: 170px;
    width: 767px; height: 601px;
    background: var(--ink-dark);
    overflow: hidden;
    color: var(--white);
  }
  .portrait-photo {
    position: absolute; left: 0; top: 0; width: 500px; height: 520px;
    background:
      linear-gradient(90deg, rgba(18,13,11,0) 0%, rgba(18,13,11,0) 62%, var(--ink-dark) 100%),
      radial-gradient(ellipse at 42% 32%, #6b4a34 0%, #4a3022 40%, #2a1a12 72%, var(--ink-dark) 100%);
  }
  .wave { position: absolute; left: 0; top: 0; width: 767px; height: 601px; }

  .nail-photo {
    position: absolute; left: 80px; top: 338px; width: 256px; height: 184px;
    transform: rotate(-8.5deg);
    background: linear-gradient(135deg, #5a3424 0%, #8a5038 45%, #c28d74 65%, #c76aa8 100%);
    box-shadow: 0 4px 10px rgba(0,0,0,.45);
  }

  .brand-name {
    position: absolute; left: 320px; top: 50px; width: 420px;
    text-align: center; white-space: nowrap;
    font-family: "Marcellus", serif; font-weight: 400; font-size: 38px; letter-spacing: 0.5px;
    color: var(--gold); line-height: 1;
  }
  .tagline {
    position: absolute; left: 320px; top: 97px; width: 420px;
    text-align: center; white-space: nowrap;
    font-family: "Ubuntu", sans-serif; font-style: italic; font-size: 22px; line-height: 26px;
  }

  .service {
    position: absolute; left: 334px;
    font-family: "Bitter", serif; font-style: italic; font-weight: 800;
    color: var(--gold-light); font-size: 34px; line-height: 31px; white-space: nowrap;
  }
  .service-head-spa { top: 170px; }
  .service-manicure { top: 228px; }
  .service-detail {
    position: absolute; left: 333px; top: 323px;
    font-family: "Ubuntu", sans-serif; font-size: 17px; line-height: 21px; white-space: nowrap;
  }

  .price-tag { position: absolute; width: 200px; height: 76px; }
  .price-tag svg { position: absolute; inset: 0; }
  .price-tag .price {
    position: absolute; left: 20px; top: 14px;
    font-family: "Noto Serif", serif; font-size: 27px; white-space: nowrap;
  }
  .price-tag .price b { font-size: 40px; font-weight: 700; }
  .price-head-spa { left: 529px; top: 142px; }
  .price-manicure { left: 529px; top: 233px; }
  .price-manicure .price { top: 12px; }

  .location {
    position: absolute; left: 347px; top: 0; width: 400px; height: 601px;
    font-style: normal; font-family: "Montserrat", sans-serif;
  }
  .location > div { position: absolute; left: 0; width: 100%; text-align: center; white-space: nowrap; }
  .location .hotel { top: 466px; font-size: 23px; font-weight: 500; line-height: 28px; }
  .location .phone { top: 500px; font-size: 34px; font-weight: 600; line-height: 40px; }
  .location .web { top: 547px; font-family: "Ubuntu", sans-serif; font-size: 18px; letter-spacing: 3px; line-height: 22px; }

  .social {
    position: absolute; left: 28px; top: 554px;
    display: flex; align-items: center; gap: 6px;
    font-family: "Ubuntu", sans-serif; font-size: 15px; white-space: nowrap;
  }
  .social .marker { width: 26px; height: 26px; border: 2px solid var(--gold); border-radius: 6px; }
</style>
</head>
<body>
  <section class="ad">
    <div class="portrait-photo" role="img" aria-label="Portrait of a woman with long wavy brown hair"></div>

    <svg class="wave" viewBox="0 0 767 601" aria-hidden="true">
      <defs>
        <linearGradient id="bandFill" x1="0" y1="0" x2="1" y2="1">
          <stop offset="0" stop-color="var(--band-shadow)"/>
          <stop offset="0.6" stop-color="var(--band-brown)"/>
          <stop offset="1" stop-color="var(--band-shadow)"/>
        </linearGradient>
      </defs>
      <path d="M0,362 C40,420 120,465 230,462 C400,455 520,385 620,397 C690,405 740,425 767,440 L767,601 L0,601 Z" fill="var(--gold)"/>
      <path d="M0,398 C50,450 130,480 240,476 C400,470 520,398 620,407 C690,413 740,432 767,450 L767,601 L0,601 Z" fill="url(#bandFill)"/>
    </svg>

    <div class="nail-photo" role="img" aria-label="Manicure scene with hands, dark nail polish, candles and orchids"></div>

    <h1 class="brand-name">SALON BRIGHTWAVE</h1>
    <p class="tagline">“Quality Care, Quality Hair”</p>

    <h2 class="service service-head-spa">Head Spa</h2>
    <div class="price-tag price-head-spa">
      <svg viewBox="0 0 200 76">
        <defs>
          <linearGradient id="bronzeTag" x1="0" x2="1">
            <stop offset="0" stop-color="var(--bronze-start)"/>
            <stop offset="1" stop-color="var(--bronze-end)"/>
          </linearGradient>
        </defs>
        <polyline points="4,4 60,8" fill="none" stroke="var(--white)" stroke-width="2"/>
        <polyline points="194,18 196,18 190,74 22,74 20,66" fill="none" stroke="var(--white)" stroke-width="2"/>
        <polygon points="2,14 193,0 178,67 10,67" fill="url(#bronzeTag)"/>
      </svg>
      <div class="price">$<b>30</b>+Tax</div>
    </div>

    <h2 class="service service-manicure">Manicure<br>Treatment<br>Course</h2>
    <div class="price-tag price-manicure">
      <svg viewBox="0 0 200 76">
        <defs>
          <linearGradient id="tealTag" x1="0" x2="1">
            <stop offset="0" stop-color="var(--teal-start)"/>
            <stop offset="1" stop-color="var(--teal-end)"/>
          </linearGradient>
        </defs>
        <polyline points="140,6 189,0 188,8" fill="none" stroke="var(--white)" stroke-width="2"/>
        <polyline points="2,20 8,74 172,74 174,68" fill="none" stroke="var(--white)" stroke-width="2"/>
        <polygon points="0,0 196,12 191,67 12,67" fill="url(#tealTag)"/>
      </svg>
      <div class="price">$<b>20</b>+Tax</div>
    </div>

    <p class="service-detail">(Filing+Cuticle Care<br>+Massage+Coloring)</p>

    <address class="location">
      <div class="hotel">Lanakila Crest Hotel 1F</div>
      <div class="phone">Call: 808-555-0173</div>
      <div class="web">salonbrightwave.example</div>
    </address>

    <div class="social">
      <span class="marker"></span>
      <span>@salonbrightwave</span>
    </div>
  </section>
</body>
</html>
```